Bright And Steady Web Design & Marketing

Will award a 2nd place prize of $100.00 if someone can come up with a logo to match this design!
Updates

Okay, I'm really looking to see some better designs here. What do you think will bring the best designs out? Please remember with all future submissions I'm looking for a cartoon style / illustrator style website. I'm not sure what the technical term is for it, so I uploaded some images in the brief.

Target Market(s)

Small Business Owners

Industry/Entity Type

Marketing

Logo Text

BrightAndSteady.example

Number of Pages Required

1 page

Colors

Designer to choose colors to be used in the design.

Requirements
Must have
• Logo should say BrightAndSteady.example I would like more than just a text logo. I want some sort of cool custom graphic / icon with it that will look nice on shirts/hats/etc

```html
<!DOCTYPE html>
<html lang="en">
<head>
<meta charset="utf-8">
<title>Bright &amp; Steady – Web Design &amp; Marketing</title>
<link href="https://fonts.googleapis.com/css2?family=Roboto+Condensed:wght@400;700&family=Roboto:wght@400;500;700&display=swap" rel="stylesheet">
<style>
:root{
  --sky:#14a9de;
  --navy:#0b4f68;
  --footer:#0e3a52;
  --orange:#ff5a1f;
  --green:#6cb52d;
  --charcoal:#3a3a3a;
  --charcoal-2:#4a4a4a;
  --charcoal-3:#5b5b5b;
  --ink:#2b2b2b;
  --grey-bg:#f2f2f2;
  --grey-text:#777;
  --white:#fff;
}
*{box-sizing:border-box;margin:0;padding:0}
html,body{width:1200px;height:5000px;overflow:hidden}
body{font-family:"Roboto",sans-serif;color:var(--ink);background:var(--white);position:relative}
section,header,footer{position:absolute;left:0;width:1200px}

/* top bar */
.topbar{position:absolute;left:0;top:0;width:1200px;height:40px;background:var(--navy);color:var(--white);font-size:15px;display:flex;align-items:center;padding:0 40px;gap:8px;z-index:3}
.topbar .social{width:18px;height:18px;background:var(--white);opacity:.9;border-radius:2px}
.topbar .phone{margin-left:14px;font-weight:500;display:flex;gap:6px;align-items:center}
.topbar .right{margin-left:auto;display:flex;gap:28px;align-items:center}
.topbar .right span{display:flex;gap:8px;align-items:center}

/* hero */
.hero{top:0;height:800px;overflow:hidden}
.hero-art{position:absolute;inset:0;background:
  radial-gradient(ellipse 900px 160px at 50% 790px,#ffffff 60%,rgba(255,255,255,0) 61%),
  linear-gradient(180deg,#0d6f93 0%,#1aa6d9 35%,#5cc6ec 70%,#cdeefa 100%)}
.rocket-art{position:absolute;left:230px;top:120px;width:230px;height:560px;border-radius:115px 115px 40px 40px;background:linear-gradient(180deg,#ffffff,#e8eef2 60%,#ffb54d 85%,rgba(255,255,255,0));opacity:.9}
.skyline-art{position:absolute;left:0;top:470px;width:1200px;height:250px;background:linear-gradient(180deg,rgba(20,120,170,0),rgba(20,120,170,.55))}
.nav{position:absolute;top:40px;left:0;width:1200px;height:110px;display:flex;align-items:center;padding:0 50px}
.brand{display:flex;align-items:center;gap:14px;color:var(--white);font-family:"Roboto Condensed",sans-serif;font-weight:700;font-size:34px;line-height:1}
.brand .mark{width:50px;height:50px;border-radius:50%;background:var(--orange)}
.menu{margin-left:auto;display:flex;gap:38px;font-weight:500;font-size:19px;color:var(--white)}
.menu .active{border-bottom:3px solid var(--white);padding-bottom:6px}
.hero-label{position:absolute;color:var(--white);font-family:"Roboto Condensed",sans-serif;font-weight:700;display:flex;align-items:center;gap:10px;white-space:nowrap}
.hero-label::before{content:"";width:14px;height:14px;border-radius:50%;background:var(--white)}
.dots{position:absolute;top:758px;left:0;width:1200px;display:flex;justify-content:center;gap:12px}
.dots i{width:16px;height:16px;border-radius:50%;border:2px solid #555;display:block}
.dots i.on{background:#333;border-color:#333}

/* common */
.section-title{font-family:"Roboto Condensed",sans-serif;font-weight:700;font-size:56px;text-align:center;color:var(--sky);letter-spacing:.5px;line-height:1.2}
.btn{display:block;margin:0 auto;width:185px;height:56px;line-height:56px;text-align:center;color:var(--white);font-weight:500;font-size:20px}
.btn-sky{background:var(--sky)}
.btn-orange{background:var(--orange)}

/* about */
.about{top:800px;height:270px;text-align:center}
.about p{width:1080px;margin:14px auto 30px;font-size:31px;line-height:1.25;color:var(--ink)}

/* services */
.services{top:1080px;height:800px}
.services .section-title{margin-top:20px}
.service-grid{position:absolute;top:130px;left:44px;display:grid;grid-template-columns:repeat(4,263px);grid-auto-rows:297px;gap:30px 20px}
.service-card{background:var(--sky);color:var(--white);text-align:center;padding:28px 16px 0;overflow:hidden}
.service-card svg{width:100px;height:100px;display:block;margin:0 auto 20px}
.service-card h3{font-size:17px;font-weight:700;margin-bottom:8px;white-space:nowrap}
.service-card p{font-size:13px;line-height:1.3;text-align:left}

/* pricing */
.pricing{top:1890px;height:620px}
.pricing .section-title{margin-top:20px}
.plans{position:absolute;top:127px;left:44px;display:grid;grid-template-columns:repeat(4,263px);gap:20px}
.plan{background:var(--grey-bg);height:450px;text-align:center}
.plan-head{height:166px;color:var(--white);padding-top:20px}
.plan-head .tier{font-size:22px}
.plan-head .price{font-size:56px;font-weight:400;line-height:1.1}
.plan-head .price sup{font-size:22px}
.plan-head .price small{font-size:16px}
.plan-head .signup{display:block;margin:8px auto 0;width:190px;height:30px;line-height:30px;background:var(--white);font-size:16px}
.plan-list{list-style:none;padding-top:30px;color:var(--grey-text);font-size:18px;line-height:31px}
.plan-save{font-weight:700;font-size:18px;margin-top:24px}
.basic .plan-head{background:var(--orange)} .basic .signup,.basic .plan-save{color:var(--orange)}
.regular .plan-head{background:var(--sky)} .regular .signup,.regular .plan-save{color:var(--sky)}
.premium .plan-head{background:var(--green)} .premium .signup,.premium .plan-save{color:var(--green)}
.ultimate .plan-head{background:var(--charcoal)} .ultimate .signup,.ultimate .plan-save{color:var(--charcoal)}

/* team */
.team{top:2550px;height:883px;background:var(--charcoal)}
.team .section-title{color:var(--white);margin-top:32px}
.team-photo{position:absolute;top:140px;left:44px;width:1112px;height:283px;background:linear-gradient(90deg,#6d5a4c,#c9b7a6 30%,#8b6e5a 55%,#d8d4cf 80%,#9aa4ad)}
.team-cards{position:absolute;top:423px;left:44px;display:grid;grid-template-columns:repeat(4,278px);height:214px}
.team-card{color:var(--white);padding:16px 20px;overflow:hidden}
.team-card:nth-child(odd){background:var(--charcoal-2)}
.team-card:nth-child(even){background:var(--charcoal-3)}
.team-card .name{font-family:"Roboto Condensed",sans-serif;font-weight:700;font-size:24px;text-align:center;margin-bottom:22px}
.team-card .role{font-family:"Roboto Condensed",sans-serif;font-weight:700;font-size:24px;margin-bottom:8px;white-space:nowrap}
.team-card p{font-size:13px;line-height:1.3}
.avatars{position:absolute;top:697px;left:44px;display:grid;grid-template-columns:repeat(8,117px);gap:21px}
.avatars div{height:117px}

/* testimonials */
.testimonials{top:3433px;height:827px}
.testimonials .section-title{color:var(--ink);margin-top:60px}
.videos{position:absolute;top:190px;left:47px;display:grid;grid-template-columns:repeat(2,546px);gap:13px}
.video{position:relative;height:356px;background:linear-gradient(135deg,#b9b3ad,#8c8781 50%,#d1ccc6)}
.video svg{position:absolute;left:50%;top:50%;width:86px;height:86px;transform:translate(-50%,-50%)}
.video-caption{background:var(--orange);color:var(--white);text-align:center;height:90px;padding-top:10px}
.video-caption strong{display:block;font-family:"Roboto Condensed",sans-serif;font-size:34px;line-height:1.1}
.video-caption span{font-size:18px}
.testimonials .btn{position:absolute;top:700px;left:507px}

/* different */
.different{top:4260px;height:440px;background:var(--sky);color:var(--white)}
.different .section-title{color:var(--white);font-size:54px;margin-top:28px}
.perks{position:absolute;top:112px;left:110px;display:grid;grid-template-columns:560px 480px;row-gap:28px}
.perk{display:flex;gap:30px}
.perk svg{flex:0 0 80px;width:80px;height:80px}
.perk h4{font-size:24px;font-weight:700;margin-bottom:4px}
.perk p{font-size:15px;line-height:1.3;max-width:310px}

/* footer */
.site-footer{top:4700px;height:300px;background:var(--footer);color:var(--white)}
.subscribe{position:absolute;top:100px;left:300px;width:600px;height:70px;border:2px solid var(--white);display:flex;align-items:center;padding:0 26px;font-size:18px}
.subscribe svg{margin-left:auto;width:44px;height:34px}
.copyright{position:absolute;top:246px;width:1200px;text-align:center;font-size:17px}
</style>
</head>
<body>

<div class="topbar">
  <span class="social"></span><span class="social"></span><span class="social"></span><span class="social"></span>
  <span class="phone">
    <svg width="16" height="16" viewBox="0 0 24 24" fill="#fff"><path d="M6.6 10.8a15 15 0 006.6 6.6l2.2-2.2c.3-.3.7-.4 1-.2 1.1.4 2.3.6 3.6.6.6 0 1 .4 1 1V20c0 .6-.4 1-1 1A17 17 0 013 4c0-.6.4-1 1-1h3.5c.6 0 1 .4 1 1 0 1.3.2 2.5.6 3.6.1.3 0 .7-.2 1z"/></svg>
    (555) 010-4567</span>
  <div class="right">
    <span><svg width="16" height="16" viewBox="0 0 24 24"><circle cx="12" cy="12" r="11" fill="#fff"/><text x="12" y="17" font-size="14" text-anchor="middle" fill="#0b4f68" font-family="Roboto,sans-serif" font-weight="700">?</text></svg>Help</span>
    <span><svg width="16" height="16" viewBox="0 0 24 24"><circle cx="12" cy="12" r="11" fill="#fff"/><circle cx="12" cy="9" r="4" fill="#0b4f68"/><path d="M5 19c2-4 12-4 14 0" fill="#0b4f68"/></svg>Sam R. Lee</span>
  </div>
</div>

<header class="hero">
  <div class="hero-art" role="img" aria-label="Cartoon illustration of a rocket launching over a city skyline with clouds"></div>
  <div class="skyline-art" role="img" aria-label="City skyline silhouette"></div>
  <div class="rocket-art" role="img" aria-label="Cartoon rocket taking off"></div>
  <nav class="nav">
    <div class="brand"><span class="mark"></span>Bright &amp; Steady</div>
    <div class="menu"><span class="active">HOME</span><span>SERVICES</span><span>PRICING</span><span>BLOG</span><span>ABOUT US</span></div>
  </nav>
  <span class="hero-label" style="left:690px;top:212px;font-size:36px">Website</span>
  <span class="hero-label" style="left:880px;top:190px;font-size:24px">Online Store</span>
  <span class="hero-label" style="left:975px;top:255px;font-size:17px">Logo &amp; Branding</span>
  <span class="hero-label" style="left:560px;top:288px;font-size:22px">Outsourcing Management</span>
  <span class="hero-label" style="left:800px;top:345px;font-size:22px">Design &amp; Management</span>
  <span class="hero-label" style="left:975px;top:385px;font-size:40px">SEO</span>
  <span class="hero-label" style="left:690px;top:440px;font-size:28px">Consulting</span>
  <span class="hero-label" style="left:840px;top:482px;font-size:22px">Social Media Marketing</span>
  <div class="dots"><i class="on"></i><i></i><i></i></div>
</header>

<section class="about">
  <h2 class="section-title">ABOUT BRIGHT &amp; STEADY</h2>
  <p>We are a family owned and operated company. Companies who take pride in their work and their customers. We want to build mutually beneficial, lucrative,</p>
  <span class="btn btn-sky">READ MORE</span>
</section>

<section class="services" id="services">
  <h2 class="section-title">OUR SERVICES</h2>
  <div class="service-grid">
    <article class="service-card">
      <svg viewBox="0 0 100 100"><circle cx="50" cy="50" r="46" fill="#fff"/><circle cx="50" cy="50" r="30" fill="none" stroke="#14a9de" stroke-width="6"/><path d="M30 40c10 0 12 8 20 6s4 14 12 16M58 24c-2 8 6 10 14 10" fill="none" stroke="#14a9de" stroke-width="6"/></svg>
      <h3>Web Design &amp; Management</h3>
      <p>To make your pages look polished, we provide header, footer, cover page, and text box designs that complement each other.</p>
    </article>
    <article class="service-card">
      <svg viewBox="0 0 100 100"><rect x="8" y="8" width="84" height="84" rx="14" fill="#fff"/><path d="M30 70l4-14 28-28 10 10-28 28z" fill="#14a9de"/></svg>
      <h3>Logo Design &amp; Branding</h3>
      <p>To make your pages look polished, we provide header, footer, cover page, and text box designs that complement each other.</p>
    </article>
    <article class="service-card">
      <svg viewBox="0 0 100 100"><path d="M6 20h14l10 44h48l10-32H26" fill="none" stroke="#fff" stroke-width="7"/><rect x="30" y="36" width="50" height="22" fill="#fff"/><circle cx="38" cy="78" r="7" fill="#fff"/><circle cx="70" cy="78" r="7" fill="#fff"/></svg>
      <h3>Online Store Design</h3>
      <p>To make your pages look polished, we provide header, footer, cover page, and text box designs that complement each other.</p>
    </article>
    <article class="service-card">
      <svg viewBox="0 0 100 100"><circle cx="42" cy="42" r="28" fill="none" stroke="#fff" stroke-width="10"/><path d="M62 62l26 26" stroke="#fff" stroke-width="14" stroke-linecap="round"/></svg>
      <h3>Local SEO Management</h3>
      <p>To make your pages look polished, we provide header, footer, cover page, and text box designs that complement each other.</p>
    </article>
    <article class="service-card">
      <svg viewBox="0 0 100 100"><circle cx="42" cy="42" r="30" fill="#fff"/><path d="M42 28v28M28 42h28" stroke="#14a9de" stroke-width="8"/><path d="M64 64l24 24" stroke="#fff" stroke-width="14" stroke-linecap="round"/></svg>
      <h3>Search Engine Optimization</h3>
      <p>To make your pages look polished, we provide header, footer, cover page, and text box designs that complement each other.</p>
    </article>
    <article class="service-card">
      <svg viewBox="0 0 100 100"><rect x="12" y="12" width="76" height="76" rx="8" fill="#fff"/></svg>
      <h3>Social Media Marketing</h3>
      <p>To make your pages look polished, we provide header, footer, cover page, and text box designs that complement each other.</p>
    </article>
    <article class="service-card">
      <svg viewBox="0 0 100 100"><path d="M10 12v78h82" fill="none" stroke="#fff" stroke-width="6"/><rect x="24" y="56" width="10" height="28" fill="#fff"/><rect x="40" y="40" width="10" height="44" fill="#fff"/><rect x="56" y="48" width="10" height="36" fill="#fff"/><rect x="72" y="28" width="10" height="56" fill="#fff"/></svg>
      <h3>Marketing Material &amp; Print</h3>
      <p>To make your pages look polished, we provide header, footer, cover page, and text box designs that complement each other.</p>
    </article>
    <article class="service-card">
      <svg viewBox="0 0 100 100" fill="#fff"><circle cx="50" cy="28" r="14"/><circle cx="22" cy="36" r="10"/><circle cx="78" cy="36" r="10"/><path d="M28 80c0-24 44-24 44 0z"/><path d="M4 76c0-18 30-20 30-8v8zM96 76c0-18-30-20-30-8v8z"/></svg>
      <h3>Outsourcing Management</h3>
      <p>To make your pages look polished, we provide header, footer, cover page, and text box designs that complement each other.</p>
    </article>
  </div>
</section>

<section class="pricing" id="pricing">
  <h2 class="section-title">PLAN &amp; PRICING</h2>
  <div class="plans">
    <div class="plan basic">
      <div class="plan-head"><div class="tier">Basic</div><div class="price"><sup>$</sup>399<small>/MO</small></div><span class="signup">Sign up</span></div>
      <ul class="plan-list"><li>Logo Design</li><li>SEO Optimation</li><li>Items 2</li><li>Items 3</li><li>Items 4</li><li>Item Item Items 5</li></ul>
      <div class="plan-save">Go annual and save $350</div>
    </div>
    <div class="plan regular">
      <div class="plan-head"><div class="tier">Regular</div><div class="price"><sup>$</sup>499<small>/MO</small></div><span class="signup">Sign up</span></div>
      <ul class="plan-list"><li>Logo Design</li><li>SEO Optimation</li><li>Items 2</li><li>Items 3</li><li>Items 4</li><li>Item Item Items 5</li></ul>
      <div class="plan-save">Go annual and save $250</div>
    </div>
    <div class="plan premium">
      <div class="plan-head"><div class="tier">Premium</div><div class="price"><sup>$</sup>699<small>/MO</small></div><span class="signup">Sign up</span></div>
      <ul class="plan-list"><li>Logo Design</li><li>SEO Optimation</li><li>Items 2</li><li>Items 3</li><li>Items 4</li><li>Item Item Items 5</li></ul>
      <div class="plan-save">Go annual and save $250</div>
    </div>
    <div class="plan ultimate">
      <div class="plan-head"><div class="tier">Ultimate</div><div class="price"><sup>$</sup>899<small>/MO</small></div><span class="signup">Sign up</span></div>
      <ul class="plan-list"><li>Logo Design</li><li>SEO Optimation</li><li>Items 2</li><li>Items 3</li><li>Items 4</li><li>Item Item Items 5</li></ul>
      <div class="plan-save">Go annual and save $250</div>
    </div>
  </div>
</section>

<section class="team" id="team">
  <h2 class="section-title">OUR TEAM</h2>
  <div class="team-photo" role="img" aria-label="Photo of four smiling team members in business attire"></div>
  <div class="team-cards">
    <div class="team-card"><div class="name">SAM R. LEE</div><div class="role">Finance</div><p>To make your pages look polished, we provide header, footer, cover page, and text box designs that complement each other.</p></div>
    <div class="team-card"><div class="name">MARA T. QUILL</div><div class="role">Chief Technical Officer</div><p>To make your pages look polished, we provide header, footer, cover page, and text box designs that complement each other.</p></div>
    <div class="team-card"><div class="name">SAM R. LEE</div><div class="role">Chief Operations Officer</div><p>To make your pages look polished, we provide header, footer, cover page, and text box designs that complement each other.</p></div>
    <div class="team-card"><div class="name">SAM R. LEE</div><div class="role">Chief Executive Officer</div><p>To make your pages look polished, we provide header, footer, cover page, and text box designs that complement each other.</p></div>
  </div>
  <div class="avatars">
    <div style="background:#8a6fb0" role="img" aria-label="Cartoon team avatar"></div>
    <div style="background:#4ab3d6" role="img" aria-label="Cartoon team avatar"></div>
    <div style="background:#e9e4da" role="img" aria-label="Cartoon team avatar"></div>
    <div style="background:#f3ecc8" role="img" aria-label="Cartoon team avatar"></div>
    <div style="background:#6b5a9a" role="img" aria-label="Cartoon team avatar"></div>
    <div style="background:#e07a4d" role="img" aria-label="Cartoon team avatar"></div>
    <div style="background:#e6e2dc" role="img" aria-label="Cartoon team avatar"></div>
    <div style="background:#d23a6a" role="img" aria-label="Cartoon team avatar"></div>
  </div>
</section>

<section class="testimonials">
  <h2 class="section-title">WHAT PEOPLE SAY ABOUT US</h2>
  <div class="videos">
    <div>
      <div class="video" role="img" aria-label="Video still of a smiling businesswoman giving a thumbs up">
        <svg viewBox="0 0 100 100"><circle cx="50" cy="50" r="44" fill="none" stroke="#fff" stroke-width="7"/><path d="M40 30l30 20-30 20z" fill="#fff"/></svg>
      </div>
      <div class="video-caption"><strong>Mara T. Quill</strong><span>CEO of Northpeak</span></div>
    </div>
    <div>
      <div class="video" role="img" aria-label="Video still of a businessman in an office">
        <svg viewBox="0 0 100 100"><circle cx="50" cy="50" r="44" fill="none" stroke="#fff" stroke-width="7"/><path d="M40 30l30 20-30 20z" fill="#fff"/></svg>
      </div>
      <div class="video-caption"><strong>Sam R. Lee</strong><span>CEO of Northpeak</span></div>
    </div>
  </div>
  <span class="btn btn-orange">READ MORE</span>
</section>

<section class="different">
  <h2 class="section-title">WHAT MAKES US DIFFERENT?</h2>
  <div class="perks">
    <div class="perk">
      <svg viewBox="0 0 100 100" fill="none" stroke="#fff" stroke-width="9"><path d="M82 40A34 34 0 0020 34"/><path d="M18 60a34 34 0 0062 6"/><path d="M16 18v18h18M84 82V64H66"/></svg>
      <div><h4>Risk Free Investmen</h4><p>If we are unable to deliver anything that we say we can we will refund you 100% of your investment.</p></div>
    </div>
    <div class="perk">
      <svg viewBox="0 0 100 100" fill="none" stroke="#fff" stroke-width="7"><path d="M30 46l16-30c8 0 10 6 8 14l-3 12h26c6 0 8 6 6 10l-8 28H30z"/><rect x="10" y="46" width="20" height="42"/></svg>
      <div><h4>Customer Loyalty Program</h4><p>After 12 months of on time payments Customers will receive cash back reward bonuses.</p></div>
    </div>
    <div class="perk">
      <svg viewBox="0 0 100 100"><circle cx="50" cy="50" r="42" fill="none" stroke="#fff" stroke-width="8"/><path d="M50 24v28l18 10" fill="none" stroke="#fff" stroke-width="8"/></svg>
      <div><h4>24/7 Support</h4><p>24/7 U.S. Based Customer Support Phone and Email.</p></div>
    </div>
    <div class="perk">
      <svg viewBox="0 0 100 100" fill="#fff"><path d="M50 8L8 30h84z"/><rect x="16" y="36" width="10" height="40"/><rect x="36" y="36" width="10" height="40"/><rect x="56" y="36" width="10" height="40"/><rect x="76" y="36" width="10" height="40"/><rect x="8" y="80" width="84" height="10"/></svg>
      <div><h4>Unmatched Personal Service</h4><p>Do you need us to come to your office to help train staff? That's not a problem. We will come to you and provide hands on training.</p></div>
    </div>
    <div class="perk">
      <svg viewBox="0 0 100 100"><rect x="6" y="22" width="88" height="58" rx="6" fill="#fff"/><rect x="6" y="34" width="88" height="10" fill="#14a9de"/><rect x="16" y="58" width="26" height="8" fill="#14a9de"/></svg>
      <div><h4>Multiple Payment Options Available</h4><p>Website Leasing, 90 Days Same As Cash, Website Financing.</p></div>
    </div>
  </div>
</section>

<footer class="site-footer">
  <div class="subscribe">Enter your email to subscribe...
    <svg viewBox="0 0 44 34"><rect x="1" y="1" width="42" height="32" fill="#fff"/><path d="M2 3l20 16L42 3" fill="none" stroke="#0e3a52" stroke-width="3"/></svg>
  </div>
  <div class="copyright">Copyright 2017 Bright &amp; Steady. All rights reserved.</div>
</footer>

</body>
</html>
```